Business Card Design Project

We need a double-sided business card design for our e-commerce company. Be as creative as you can.

Reason: Change of logo

Target Market(s)

Business owners

Industry/Entity Type

E-Commerce

Requirements
Must have
• Name (editable)
Mobile number -editable
www.trizvo.com - MUST STAND OUT ALONE
Office address:
27 Pellow Road
#09-04 Corbell Tower
Singapore 058214

```html
<!DOCTYPE html>
<html lang="en">
<head>
<meta charset="utf-8">
<title>Trizvo Business Card</title>
<link rel="stylesheet" href="https://fonts.googleapis.com/css2?family=Archivo:wght@500;700&family=Open+Sans:wght@400;600&display=swap">
<style>
  :root {
    --orange: #f98d00;
    --orange-deep: #f47f00;
    --orange-glow: #ffb700;
    --white: #ffffff;
    --ink: #1a1a1a;
    --rule: #6f6f6f;
    --stage: #e4e4e4;
  }
  * { box-sizing: border-box; margin: 0; padding: 0; }
  html, body { width: 1200px; height: 800px; overflow: hidden; }
  body {
    background: var(--stage);
    font-family: "Open Sans", Arial, sans-serif;
    position: relative;
  }
  .card {
    position: absolute;
    width: 530px;
    height: 304px;
    border-radius: 38px;
    overflow: hidden;
    box-shadow: 0 10px 24px rgba(0,0,0,0.18);
  }
  .card-front {
    left: 45px;
    top: 248px;
    background: radial-gradient(ellipse at 50% 50%, var(--orange-glow) 0%, var(--orange) 55%, var(--orange-deep) 100%);
    display: flex;
    align-items: center;
    justify-content: center;
  }
  .front-brand {
    font-family: "Archivo", Arial, sans-serif;
    font-weight: 700;
    font-size: 72px;
    color: var(--white);
    letter-spacing: 1px;
  }
  .card-back {
    left: 625px;
    top: 248px;
    background: var(--white);
  }
  .back-brand {
    position: absolute;
    left: 34px;
    top: 22px;
    font-family: "Archivo", Arial, sans-serif;
    font-weight: 700;
    font-size: 46px;
    color: var(--orange);
    line-height: 1;
  }
  .office-address {
    position: absolute;
    left: 214px;
    top: 44px;
    font-size: 11.5px;
    line-height: 1.3;
    color: var(--orange);
    font-style: normal;
  }
  .identity {
    position: absolute;
    left: 40px;
    top: 124px;
    width: 200px;
    text-align: right;
  }
  .person-name {
    font-family: "Archivo", Arial, sans-serif;
    font-weight: 700;
    font-size: 17px;
    color: var(--orange);
    letter-spacing: -0.2px;
  }
  .person-role {
    font-size: 12.5px;
    color: var(--ink);
    margin-top: 1px;
    padding-right: 52px;
  }
  .divider {
    position: absolute;
    left: 265px;
    top: 116px;
    width: 1.5px;
    height: 106px;
    background: var(--rule);
  }
  .contact-list {
    position: absolute;
    left: 300px;
    top: 158px;
    list-style: none;
    font-size: 13px;
    color: var(--ink);
  }
  .contact-list li {
    display: flex;
    align-items: center;
    gap: 8px;
    height: 24px;
  }
  .contact-list svg { width: 14px; height: 14px; flex: none; }
  .footer-band {
    position: absolute;
    left: 0;
    bottom: 0;
    width: 530px;
    height: 62px;
  }
  .website {
    position: absolute;
    right: 52px;
    bottom: 14px;
    display: flex;
    align-items: center;
    gap: 8px;
    font-size: 12.5px;
    color: var(--white);
  }
  .website svg { width: 16px; height: 16px; }
</style>
</head>
<body>

  <section class="card card-front" aria-label="Card front">
    <span class="front-brand">trizvo</span>
  </section>

  <section class="card card-back" aria-label="Card back">
    <span class="back-brand">trizvo</span>
    <address class="office-address">
      27 Pellow Road, #09-04 Corbell Tower<br>
      <strong>Singapore</strong> 058214
    </address>

    <div class="identity">
      <p class="person-name">YOUR COMPLETE NAME</p>
      <p class="person-role">Your Position</p>
    </div>

    <span class="divider"></span>

    <ul class="contact-list">
      <li>
        <svg viewBox="0 0 24 24" aria-hidden="true"><path fill="var(--orange)" d="M6.6 10.8a15.1 15.1 0 0 0 6.6 6.6l2.2-2.2c.3-.3.7-.4 1-.2 1.1.4 2.3.6 3.6.6.6 0 1 .4 1 1V20c0 .6-.4 1-1 1A17 17 0 0 1 3 4c0-.6.4-1 1-1h3.5c.6 0 1 .4 1 1 0 1.3.2 2.5.6 3.6.1.3 0 .7-.2 1z"/></svg>
        <span>123-456-7890</span>
      </li>
      <li>
        <svg viewBox="0 0 24 24" aria-hidden="true"><path fill="none" stroke="var(--orange)" stroke-width="2" d="M3 9l9-6 9 6v11H3z M3 9l9 6 9-6"/></svg>
        <span>emailme@myaddress.com</span>
      </li>
    </ul>

    <svg class="footer-band" viewBox="0 0 530 62" preserveAspectRatio="none" aria-hidden="true">
      <path fill="var(--orange)" d="M0 10 L305 26 C318 27 320 8 336 8 L530 8 L530 62 L0 62 Z"/>
    </svg>
    <div class="website">
      <svg viewBox="0 0 24 24" aria-hidden="true"><g fill="none" stroke="var(--white)" stroke-width="1.8"><circle cx="12" cy="12" r="9"/><ellipse cx="12" cy="12" rx="4" ry="9"/><path d="M3 12h18M5 7h14M5 17h14"/></g></svg>
      <span>www.trizvo.com</span>
    </div>
  </section>

</body>
</html>
```